Owen Tasker Studios Business Card

Looking for a clear, modern, elegant, sharp business card that conveys a professional yet edgy image to my business as a wedding, portrait, and travel photographer. Would like something that looks vintage yet modern. Need a new business card to grow my business. We are growing the business for Wedding and Event Photography as well as fine art Photography. (Mostly Landscapes)
Updates

I’m looking through designs now but I have a new logo that i want using please.

New logo uploaded please redesign using that

PLEASE ALL DESIGNERS LOOK IN BRIEF FOR NEW LOGO

Target Market(s)

Brides, Grooms, Families with Kids, People looking for Fine Art Photography Artwork

Industry/Entity Type

Photographer

Contact Information for Business Card

Unsure

Font styles to use
Serif

Colors

Designer to choose colors to be used in the design.

Requirements
Must have
• My Website:
• http://taskerlens.examplefolio.net
• Phone:
• 323-481-5206
• Email:
• owentaskerlens@mailbox-example.net
Nice to have
• Would like a sort of shine on the printing finish.
• I like black I think it looks good on a business card.
• Can try working with my logo (png that I've attached)

```html
<!DOCTYPE html>
<html lang="en">
<head>
<meta charset="utf-8">
<title>Owen Tasker Studios Business Card</title>
<link href="https://fonts.googleapis.com/css2?family=Josefin+Sans:wght@400&family=Source+Sans+3:wght@400&display=swap" rel="stylesheet">
<style>
  :root {
    --backdrop: #2b2b2b;
    --card: #060606;
    --ink: #f4f4f4;
    --rule: #ffffff;
  }
  * { margin: 0; padding: 0; box-sizing: border-box; }
  html, body { width: 1200px; height: 900px; overflow: hidden; }
  body { background: var(--backdrop); position: relative; }

  .card {
    position: absolute;
    width: 600px;
    height: 343px;
    background: var(--card);
    box-shadow: 0 14px 30px rgba(0,0,0,.55);
    overflow: hidden;
  }
  .card--front { left: 70px; top: 70px; }
  .card--back { left: 530px; top: 487px; }

  .rule { position: absolute; height: 3px; background: var(--rule); }

  .brand {
    position: absolute;
    text-align: center;
    color: var(--ink);
    font-family: "Josefin Sans", sans-serif;
    font-weight: 400;
  }
  .brand__name { display: block; font-size: 26px; letter-spacing: 6px; line-height: 1; }
  .brand__sub { display: block; font-size: 8px; letter-spacing: 5px; margin-top: 5px; }

  /* front */
  .card--front .rule { left: 0; top: 168px; width: 468px; }
  .card--front .brand { right: 40px; top: 184px; }

  /* back */
  .card--back .brand { right: 38px; top: 40px; }
  .person {
    position: absolute;
    right: 44px;
    top: 132px;
    text-align: right;
    color: var(--ink);
    font-family: "Source Sans 3", sans-serif;
    font-size: 15px;
    line-height: 19px;
  }
  .person__name { text-transform: uppercase; letter-spacing: .5px; }
  .card--back .rule--top { left: 0; top: 180px; width: 430px; }
  .card--back .rule--tick { right: 0; top: 140px; width: 22px; }
  .card--back .rule--bottom { left: 0; top: 298px; width: 372px; }

  .contacts {
    position: absolute;
    right: 14px;
    top: 192px;
    list-style: none;
    color: var(--ink);
    font-family: "Source Sans 3", sans-serif;
    font-size: 15px;
  }
  .contacts li {
    display: flex;
    justify-content: flex-end;
    align-items: center;
    gap: 10px;
    height: 24px;
  }
  .contacts svg { width: 13px; height: 13px; flex: none; }
</style>
</head>
<body>

  <section class="card card--front" aria-label="Card front">
    <div class="rule"></div>
    <div class="brand">
      <span class="brand__name">OWEN TASKER</span>
      <span class="brand__sub">STUDIOS</span>
    </div>
  </section>

  <section class="card card--back" aria-label="Card back">
    <div class="brand">
      <span class="brand__name">OWEN TASKER</span>
      <span class="brand__sub">STUDIOS</span>
    </div>
    <div class="rule rule--tick"></div>
    <div class="person">
      <div class="person__name">Marcus Delano</div>
      <div class="person__role">Photographer</div>
    </div>
    <div class="rule rule--top"></div>
    <ul class="contacts">
      <li>323-481-5206
        <svg viewBox="0 0 24 24" aria-hidden="true"><path fill="#fff" d="M6.6 10.8a15.2 15.2 0 0 0 6.6 6.6l2.2-2.2c.3-.3.7-.4 1-.2 1.1.4 2.3.6 3.6.6.6 0 1 .4 1 1V20c0 .6-.4 1-1 1A17 17 0 0 1 3 4c0-.6.4-1 1-1h3.5c.6 0 1 .4 1 1 0 1.3.2 2.5.6 3.6.1.3 0 .7-.2 1z"/></svg>
      </li>
      <li>owentaskerlens@mailbox-example.net
        <svg viewBox="0 0 24 24" aria-hidden="true"><rect x="2" y="5" width="20" height="14" fill="#fff"/><path d="M2 5l10 8 10-8" fill="none" stroke="#060606" stroke-width="1.8"/></svg>
      </li>
      <li>http://taskerlens.examplefolio.net
        <svg viewBox="0 0 24 24" aria-hidden="true"><g fill="none" stroke="#fff" stroke-width="1.8"><circle cx="12" cy="12" r="9"/><ellipse cx="12" cy="12" rx="4" ry="9"/><path d="M3 12h18M5 7h14M5 17h14"/></g></svg>
      </li>
    </ul>
    <div class="rule rule--bottom"></div>
  </section>

</body>
</html>
```